Classy, Elegant, Simple Business Card Design

Looking to have a classy, simple, and elegant design. Want a top notch designed business card. I really like the look of the new veltro credit card. I also like the design I attached. I am trying to reach 21-29 year old females for booking us for there wedding or event. We offer Disc Jockey Service, Photo Booth Rentals, and Uplighting .

Target Market(s)

21-28 year old females

Contact Information for Business Card

Has to have logo, website, email, and phone number

Font styles to use
Other font styles liked:
• open to font choice, modern, clean
Designer to choose
33a6d7
0791cd
0555a3
ffffff

Requirements
Must have
• Has to have logo, website, email, and phone number
Nice to have
• I really like the design of the new veltro credit card. I also included my logo and some designs I like
Should not have
• clutter or too much info

```html
<!DOCTYPE html>
<html lang="en">
<head>
<meta charset="UTF-8">
<title>Tidelight Event Group – Business Card</title>
<link rel="stylesheet" href="https://fonts.googleapis.com/css2?family=Poppins:wght@300;400;500;600&display=swap">
<style>
  :root {
    --sky: #33a6d7;
    --azure: #0791cd;
    --royal: #0555a3;
    --navy: #0a3f7a;
    --white: #ffffff;
    --ink: #3a3d42;
    --muted: #8a8e94;
    --rule: #6f737a;
    --backdrop: #d9dadc;
  }
  * { box-sizing: border-box; margin: 0; padding: 0; }
  html, body { width: 1200px; height: 800px; overflow: hidden; }
  body {
    background: var(--backdrop);
    font-family: "Poppins", sans-serif;
    position: relative;
  }
  .card {
    position: absolute;
    width: 540px;
    height: 309px;
    overflow: hidden;
    box-shadow: 0 6px 18px rgba(0,0,0,0.18);
  }
  /* Front */
  .card-front { left: 50px; top: 110px; background: var(--white); }
  .brand {
    position: absolute; left: 36px; top: 44px;
    display: flex; align-items: center; gap: 10px;
    color: var(--azure); font-weight: 600;
  }
  .brand-dot { width: 14px; height: 14px; border-radius: 50%; background: var(--azure); }
  .brand-name { font-size: 28px; line-height: 1; letter-spacing: 0.5px; }
  .brand-sub {
    display: block; font-size: 10px; letter-spacing: 5px;
    text-transform: uppercase; margin-top: 6px;
  }
  .holder {
    position: absolute; right: 36px; top: 40px; text-align: right;
  }
  .holder-name { font-size: 20px; font-weight: 500; color: var(--azure); line-height: 1.2; }
  .holder-title { font-size: 11px; font-weight: 300; color: var(--muted); letter-spacing: 0.5px; }
  .holder-rule {
    position: absolute; right: 36px; top: 92px;
    width: 330px; height: 1px; background: var(--rule);
  }
  .contact { position: absolute; left: 36px; top: 196px; width: 250px; }
  .contact-rule { height: 1px; background: var(--rule); width: 210px; margin-bottom: 10px; }
  .contact-line {
    display: flex; align-items: center; gap: 8px;
    font-size: 13px; color: var(--ink); line-height: 22px;
  }
  .contact-line svg { width: 12px; height: 12px; fill: var(--azure); flex: none; }
  .band { position: absolute; left: 0; bottom: 0; width: 540px; height: 50px; }
  .website {
    position: absolute; right: 22px; bottom: 11px;
    font-size: 12px; color: var(--white); letter-spacing: 0.3px;
  }
  /* Back */
  .card-back {
    left: 610px; top: 380px;
    background: linear-gradient(135deg, #0a63b4 0%, var(--royal) 60%, #044a8f 100%);
  }
  .back-brand {
    position: absolute; left: 0; right: 0; top: 96px;
    text-align: center; color: var(--sky);
    font-size: 56px; font-weight: 600; letter-spacing: 1px;
  }
  .services {
    position: absolute; left: 0; right: 0; bottom: 34px;
    text-align: center; color: var(--white);
    font-size: 13px; font-weight: 400; letter-spacing: 0.3px;
  }
</style>
</head>
<body>

<section class="card card-front" aria-label="Business card front">
  <div class="brand">
    <span class="brand-dot"></span>
    <div>
      <span class="brand-name">Tidelight</span>
      <span class="brand-sub">Event Group</span>
    </div>
  </div>

  <div class="holder">
    <p class="holder-name">Daniel Reyes</p>
    <p class="holder-title">President</p>
  </div>
  <div class="holder-rule"></div>

  <div class="contact">
    <div class="contact-rule"></div>
    <p class="contact-line">
      <svg viewBox="0 0 24 24" aria-hidden="true"><path d="M6.6 10.8a15.2 15.2 0 0 0 6.6 6.6l2.2-2.2a1 1 0 0 1 1-.25 11.4 11.4 0 0 0 3.6.57 1 1 0 0 1 1 1V20a1 1 0 0 1-1 1A17 17 0 0 1 3 4a1 1 0 0 1 1-1h3.5a1 1 0 0 1 1 1c0 1.25.2 2.45.57 3.57a1 1 0 0 1-.25 1z"/></svg>
      555-014-2738
    </p>
    <p class="contact-line">
      <svg viewBox="0 0 24 24" aria-hidden="true"><path d="M2 5h20v14H2z M3.5 6.5 12 13l8.5-6.5" fill="var(--azure)" stroke="var(--white)" stroke-width="1.6"/></svg>
      hello@tidelightevents.com
    </p>
  </div>

  <svg class="band" viewBox="0 0 540 50" aria-hidden="true">
    <polyline points="0,37 322,37 334,6 540,6" fill="none" stroke="var(--navy)" stroke-width="2.5"/>
    <path d="M0,42 L326,42 L338,10 L540,10 L540,50 L0,50 Z" fill="var(--azure)"/>
  </svg>
  <p class="website">www.tidelightevents.com</p>
</section>

<section class="card card-back" aria-label="Business card back">
  <p class="back-brand">Tidelight</p>
  <p class="services">Disc Jockey Service &bull; Photo Booth Rentals &bull; Uplighting .</p>
</section>

</body>
</html>
```